Invitation reopening cosmetics studio

On April 28, we will start the reopening of the cosmetically studio and brew a flyer. In the supplement: - two pictures of mine - my idea of ​​flyer presentation - various logos - brochures as thought aid - 20% to the reopening -28.04.2018 from 10.00 - 20.00 o'clock - Studio is small but charming On April 28 we will reopen the opening of the cosmetically studio start and brew a flyer. In the supplement: - two pictures of mine - my idea of ​​flyer presentation - various logos - brochures as thought aid - 20% to the reopening -28.04.2018 from 10.00 - 20.00 o'clock - Studio is small but charming On April 28 we will reopen the opening of the cosmetically studio start and brew a flyer. In the supplement: - two pictures of mine - my idea of ​​flyer presentation - various logos - brochures as thought aid - 20% for reopening - 28.04.2018 from 10.00 - 20.00 o'clock - Studio is small but charming on 28. April we will start the reopening of the cosmetically studio and brew a flyer. In the supplement: - two pictures of mine - my idea of ​​flyer presentation - various logos - brochures as thought aid - 20% to the reopening -28.04.2018 from 10.00 - 20.00 o'clock - Studio is small but charming On April 28 we will reopen the opening of the cosmetically studio start and brew a flyer. In the supplement: - two pictures of mine - my idea of ​​flyer presentation - various logos - brochures as thought aid - 20% to the reopening -28.04.2018 from 10.00 - 20.00 o'clock - Studio is small but charming On April 28 we will reopen the opening of the cosmetically studio start and brew a flyer. In the supplement: - two pictures of mine - my idea of ​​flyer presentation - various logos - brochures as thought aid - 20% for reopening - 28.04.2018 from 10.00 - 20.00 o'clock - Studio is small but charming on 28. April we will start the reopening of the cosmetically studio and brew a flyer. In the supplement: - two pictures of mine - my idea of ​​flyer presentation - various logos - brochures as thought aid - 20% to the reopening -28.04.2018 from 10.00 - 20.00 o'clock - Studio is small but charming On April 28 we will reopen the opening of the cosmetically studio start and brew a flyer. In the supplement: - two pictures of mine - my idea of ​​flyer presentation - various logos - brochures as thought aid - 20% for reopening - 28.04.2018 from 10.00 - 20.00 o'clock - Studio is small but charming Medical cosmetics facials with high quality products Velmorine body treatments Depilation Pedicure Manicure Skin Analysis Medical Cosmetics Facials with high quality products Velmorine Body Treatments Depilation

Target Market(s)

Medical Cosmetics Facials with high quality products Velmorine Body Treatments Depilation Pedicure Manicure Skin Analysis Medical Cosmetics Facials with high quality products Velmorine Body Treatments Depilation

Industry/Entity Type

Cosmetic

Font styles to use
Sans Serif

Colors
fece3e
fee18a

Requirements
Must have
• The key data simple and simple, elegant, charming,
Nice to have
• Picture of me, when, where, personal, location, picture of me, when, where, personal, location, picture of me, when, where, personal, location, picture of me, when, where, personal, location, picture of me, when, where, personal, location, picture of me, when, where, personal, location,
Should not have
• different color, too full, different color, too full, different color, too full, different color, too full, different color, too full, different color, too full, different color, too full, different color, too full, different color , too full, different color, too full, different color, too full, different color, too full, different color, too full, different color, too full, different color, too full, different color, too full, different color, too full v

```html
<!DOCTYPE html>
<html lang="de">
<head>
<meta charset="utf-8">
<title>Lumora – Neueröffnung</title>
<link rel="stylesheet" href="https://fonts.googleapis.com/css2?family=Lato:wght@300;400;700;900&display=swap">
<style>
  :root {
    --gold: #ae9a60;
    --ink: #1a1a1a;
    --paper: #ffffff;
    --photo-dark: #2a3330;
    --photo-mid: #4d5a52;
    --dress: #1f3f86;
  }
  html, body {
    margin: 0;
    padding: 0;
    width: 1200px;
    height: 967px;
    overflow: hidden;
    background: var(--paper);
    font-family: "Lato", sans-serif;
    color: var(--ink);
  }
  .canvas { position: relative; width: 1200px; height: 967px; }
  .card {
    position: absolute;
    top: 67px;
    width: 492px;
    height: 837px;
    background: var(--paper);
    box-shadow: 0 0 3px rgba(0,0,0,0.35);
    overflow: hidden;
  }
  .card--front { left: 91px; }
  .card--back { left: 622px; }

  .portrait {
    position: absolute; left: 0; top: 0; width: 492px; height: 699px;
    background:
      radial-gradient(ellipse 38% 30% at 52% 42%, #6a4a40 0%, transparent 70%),
      radial-gradient(ellipse 55% 40% at 62% 80%, var(--dress) 0%, transparent 75%),
      linear-gradient(160deg, var(--photo-mid) 0%, var(--photo-dark) 60%, #3b4640 100%);
  }
  .brand-band {
    position: absolute; left: 0; top: 702px; width: 492px; height: 135px;
    background: var(--gold);
    display: flex; align-items: center; justify-content: center; gap: 16px;
    color: var(--paper);
  }
  .brand-mark {
    width: 64px; height: 64px; border-radius: 50%;
    border: 2px solid currentColor; box-sizing: border-box;
  }
  .brand-name {
    font-weight: 300; font-size: 42px; letter-spacing: 3px; text-transform: lowercase;
  }

  .back-brand {
    position: absolute; left: 0; right: 0; top: 57px;
    display: flex; align-items: center; justify-content: center; gap: 16px;
    color: var(--gold);
  }
  .back-brand .brand-mark { width: 66px; height: 66px; }

  .tagline {
    position: absolute; left: 0; right: 0; top: 182px;
    text-align: center; font-size: 25px; font-weight: 300; margin: 0;
  }
  .event-date {
    position: absolute; left: 196px; top: 263px; margin: 0;
    font-size: 38px; font-weight: 900; color: var(--gold); letter-spacing: 1px;
  }
  .event-time {
    position: absolute; left: 197px; top: 311px; margin: 0;
    font-size: 22px; font-weight: 900; color: var(--gold); letter-spacing: 1px;
  }
  .offer {
    position: absolute; left: 0; right: 0; top: 350px; margin: 0;
    text-align: center; font-size: 35px; font-weight: 300;
  }
  .services {
    position: absolute; left: 197px; top: 438px; margin: 0; padding: 0;
    list-style: none; font-size: 14.5px; font-weight: 300; line-height: 15px;
  }
  .services li { margin-bottom: 7.5px; }
  .divider {
    position: absolute; left: 50px; top: 692px; width: 391px; height: 0;
    border-top: 1.5px solid var(--gold);
  }
  .contact {
    position: absolute; top: 717px; margin: 0;
    font-size: 14px; font-weight: 400; line-height: 19px; font-style: normal;
  }
  .contact--address { left: 51px; }
  .contact--web { left: 289px; top: 736px; }
</style>
</head>
<body>
<div class="canvas">
  <section class="card card--front">
    <div class="portrait" role="img" aria-label="Portrait photo of the studio owner in a blue dress among green foliage"></div>
    <div class="brand-band">
      <span class="brand-mark"></span>
      <span class="brand-name">lumora</span>
    </div>
  </section>

  <section class="card card--back">
    <div class="back-brand">
      <span class="brand-mark"></span>
      <span class="brand-name">lumora</span>
    </div>
    <p class="tagline">Studio ist Klein aber charmant</p>
    <p class="event-date">28.04.2018</p>
    <p class="event-time">10.00-20.00</p>
    <p class="offer">-20% zur Neueröffnung</p>
    <ul class="services">
      <li>Medizinische Kosmetik</li>
      <li>Gesichtsbehandlungen<br>mit hochwertigen Produkten</li>
      <li>Velmorine</li>
      <li>Bodybehandlungen</li>
      <li>Enthaarung</li>
      <li>Pedicure</li>
      <li>Manicure</li>
      <li>Hautanalyse</li>
    </ul>
    <div class="divider"></div>
    <address class="contact contact--address">
      Seeweg 12, 8750 Talberg<br>
      Tel. + 41 55 610 47 29<br>
      Nat. + 41 79 408 16 52
    </address>
    <address class="contact contact--web">
      E-Mail: kontakt@lumora-k.ch<br>
      iNet: www.lumora-k.ch
    </address>
  </section>
</div>
</body>
</html>
```